Can you make FairlyNeat look better than average? We need business cards and a logo refresh :-)

REVISED BRIEF

PRIORITY

VECTOR LOGO

Create a vector version of our existing logo. The logo must not change from its current design, weight or font.

Deliverables

- Logo in blue (#2540BB)
- Logo in white (#FFFFFF)
- Logo in grey (#36454F)
- All logos on transparent background
- All logos in PNG & SVG formats. (SVG must NOT distort stroke width when resized)

BRAND MARK

Create a brand mark for use with the logo. This should be possible to used with the logo and on its own as a stand alone graphical device that represents the FAIRLYNEAT brand.

https://quellbrik.com/resources/glossary/what-is-a-brand-mark

Deliverables

- Brand Mark in blue (#2540BB)
- Brand Mark in white (#FFFFFF)
- Brand Mark in grey (#36454F)
- Brand Mark on transparent background
- Brand Mark in PNG & SVG formats. (SVG must NOT distort stroke width when resized)
- Logo combined with Brand Mark (colours and formats)
.

Business Card Layout

Create 2 layouts with the following details:-

Marcus Delaney
Co-Founder & Chief Product Officer

marcus@fairlyneat.nz
www.fairlyneat.nz
0279831465

Callum Ferris
Founder & CEO

hello@fairlyneat.nz
www.fairlyneat.nz
021 684 2590

DESIGN CONSIDERATIONS

Create versions with ‘Shaping Causes With Heart’ tag line incorporated within the design and without (maintain separation of logo from tag line)

- Create a version with and without the brand mark
- Keep it clean and simple but elevate the design with subtle design effects
- Consider use of raised spot gloss colour (this can be white on white for subtle or blue on blue or blue on white)
- Consider use of spot gloss colour (this can be white on white for subtle or blue on blue or blue on white)
- Consider use of letterpress indentation
- Ensure contact details are legible, use sans-serif font

PREVIOUS BRIEF

We need a business card design for our business FairlyNeat. We are a purpose driven brand and media agency that helps brands and charities plan and buy traditional media campaigns (TV, Radio, Print, Outdoor etc). We give a significant amount of the media booking fees we receive from media vendors to charity in the name of our clients. https://www.plinkwork.com/posts/wearefairlyneat_giveback-fairlyneat-shapingcauseswithheart-activity-5829170364418205731-Rtqe

Our strapline is 'Shaping Causes With Heart'.

We want to keep our logo design as it is but it does need tightening up and made into a proper vector image as it's been created from a font.

Our brand colour is #2540BB and we need to keep this.

Our brand is professional but human, warm and engaging and doesn't take itself too seriously.

Things We Need
- vectorisation and tidying up of existing logo
- We'd like you to think about how we can incorporate a brand mark with the logo to add another dimension to our brand
- business card layout and design
- we'll be using zentiprint.com to print the cards so please take a look at the options they have (spot gloss, foil, letterpress, square cards and even the backs of the cards can have a different design on every single card!
- potential opportunity for different famous quotes on the back or imagery or slight design differences
- we'd be open to the use of an emoji or emojiis as the brandmark or to be incorporated into the card designs
- we can have as many different design batches as we like for the backs of the cards

https://www.zentiprint.com/au/business-cards

We want to make an impact, we want to be seen as professional but fun, we want to be different.

Here's a press release of what we're about.

https://adwirely.co.nz/movings-shakings/fairlyneat-welcomes-marcus-delaney-as-co-founder/

Be bold, be different, there is no such thing as a bad idea. We're open to anything so please bring your best ideas and have fun with it! Go crazy if you like!
____________
Marcus Delaney
marcus@fairlyneat.nz
0279831465

Callum Ferris
Founder & CEO
hello@fairlyneat.nz
021 684 2590

Shaping Causes With Heart

________

These are the only details we MUST have on the cards, the rest is up to you. Just make sure you use all of your creativity but don't feel the need to crowd the card with too much, let it breathe as well.

In terms of font for the details, we'll leave that up to you, just ensure it's legible. Oh and please don't take any design inspiration from our website - that will be changing!

Please don't let the design and layout look cheap and tacky though. It needs to still feel premium but personable.

Thanks

Marcus

Many designs are changing the logo and this was NOT in the brief. We need a brand mark to complement the logo. We need to see the logo with and without the brand mark. We need to see the business card with both logo + brand mark and logo on its own We need to see the business card with and without the tagline 'Shaping Causes With Heart'

purpose driven Brand & Media Agency

Shaping Causes With Heart
Marcus Delaney, Co-Founder & Chief Product Officer, marcus@fairlyneat.nz fairlyneet.nz, 0279 831 465

Callum Ferris, Founder & CEO hello@fairlyneat.nz, fairlyneet.nz, 021 684 2590

Serif
Sans Serif

0054AA
0677BA
7BADD7
CADEEF
E8F1F8

• brand mark, vector version of existing logo, Shaping Causes With Heart tagline, existing logo traced and vectorised. Must fully explore the design options from zentiprint.com that can enhance the overall card design
• brandmark to help elevate the logo, maybe incorporate some other design elements into the card like lines, or grids.
• A cheap look and feel

```html
<!DOCTYPE html>
<html lang="en">
<head>
<meta charset="utf-8">
<title>FairlyNeat Business Card</title>
<link rel="stylesheet" href="https://fonts.googleapis.com/css2?family=Montserrat:wght@400;700&display=swap">
<style>
  :root {
    --brand-blue: #2540BB;
    --pattern-blue: #2B43C2;
    --ink: #222222;
    --paper: #FFFFFF;
    --stage: #3A3A3C;
  }
  * { margin: 0; padding: 0; box-sizing: border-box; }
  html, body {
    width: 1200px;
    height: 998px;
    overflow: hidden;
    background: var(--stage);
    font-family: "Montserrat", sans-serif;
  }
  .canvas {
    position: relative;
    width: 1200px;
    height: 998px;
  }
  .card {
    position: absolute;
    left: 250px;
    width: 700px;
    height: 400px;
    overflow: hidden;
  }
  .card--front { top: 64px; background: var(--pattern-blue); }
  .card--back  { top: 534px; background: var(--paper); }

  .pattern-area {
    position: absolute;
    inset: 0;
    background: linear-gradient(135deg, #2F48C8 0%, #2A41BE 50%, #2E46C6 100%);
  }

  .wordmark {
    position: absolute;
    font-weight: 700;
    line-height: 1;
    letter-spacing: 0;
  }
  .wordmark--front {
    left: 160px;
    top: 150px;
    font-size: 58px;
    color: var(--paper);
  }
  .tagline {
    position: absolute;
    left: 250px;
    top: 258px;
    font-size: 25px;
    font-weight: 400;
    color: var(--paper);
    letter-spacing: 0.5px;
  }

  .wordmark--back {
    left: 64px;
    top: 122px;
    font-size: 54px;
    color: var(--brand-blue);
  }

  .contact {
    position: absolute;
    left: 392px;
    top: 218px;
    color: var(--ink);
  }
  .contact__name {
    font-size: 25px;
    font-weight: 700;
    color: var(--brand-blue);
    margin-bottom: 4px;
  }
  .contact__role {
    font-size: 15px;
    font-weight: 400;
    margin-bottom: 6px;
  }
  .contact__list { list-style: none; }
  .contact__item {
    display: flex;
    align-items: center;
    gap: 10px;
    font-size: 16px;
    font-weight: 400;
    line-height: 26px;
  }
  .contact__icon { width: 16px; height: 16px; flex: none; fill: var(--brand-blue); }
</style>
</head>
<body>
<main class="canvas">
  <section class="card card--front">
    <div class="pattern-area" role="img" aria-label="Repeating geometric cube line pattern in deep blue"></div>
    <p class="wordmark wordmark--front">FairlyNeat</p>
    <p class="tagline">Shaping Causes With Heart</p>
  </section>

  <section class="card card--back">
    <p class="wordmark wordmark--back">FairlyNeat</p>
    <div class="contact">
      <p class="contact__name">Marcus Delaney</p>
      <p class="contact__role">Co-Founder &amp; Chief Product Officer</p>
      <ul class="contact__list">
        <li class="contact__item">
          <svg class="contact__icon" viewBox="0 0 24 24" aria-hidden="true"><path d="M6.6 10.8a15.1 15.1 0 0 0 6.6 6.6l2.2-2.2a1 1 0 0 1 1-.25 11.4 11.4 0 0 0 3.6.57 1 1 0 0 1 1 1V20a1 1 0 0 1-1 1A17 17 0 0 1 3 4a1 1 0 0 1 1-1h3.5a1 1 0 0 1 1 1c0 1.250.2 2.45.57 3.6a1 1 0 0 1-.25 1z"/></svg>
          <span>0279831465</span>
        </li>
        <li class="contact__item">
          <svg class="contact__icon" viewBox="0 0 24 24" aria-hidden="true"><path d="M2 5h20v14H2z M4 7v.5l8 5 8-5V7l-8 5z" fill-rule="evenodd"/></svg>
          <span>marcus@fairlyneat.nz</span>
        </li>
        <li class="contact__item">
          <svg class="contact__icon" viewBox="0 0 24 24" aria-hidden="true"><path d="M12 2a10 10 0 1 0 0 20 10 10 0 0 0 0-20zm0 2c.9 0 2.1 1.8 2.6 5H9.4C9.9 5.8 11.1 4 12 4zM4.3 11h3c0 .7 0 1.3.1 2h-3a8 8 0 0 1-.1-2zm.4 4h2.9c.3 1.5.8 2.8 1.4 3.8A8 8 0 0 1 4.7 15zm2.9-6H4.7a8 8 0 0 1 4.3-3.8c-.6 1-1.1 2.3-1.4 3.8zM12 20c-.9 0-2.1-1.8-2.6-5h5.2c-.5 3.2-1.7 5-2.6 5zm-2.8-7a16 16 0 0 1 0-2h5.6a16 16 0 0 1 0 2zm5.8 5.8c.6-1 1.1-2.300 1.4-3.8h2.9a8 8 0 0 1-4.3 3.8zM16.6 13a17 17 0 0 0 0-2h3a8 8 0 0 1 0 2zm-.2-4c-.3-1.5-.8-2.8-1.4-3.8A8 8 0 0 1 19.3 9z"/></svg>
          <span>www.fairlyneat.nz</span>
        </li>
      </ul>
    </div>
  </section>
</main>
</body>
</html>
```